Brivora Collective Business Card Design

We need a business card design for Brivora Collective. We are a healthcare recruiting, wellness and education company. We partner with medical facilities to find quality candidates. We also offer free wellness courses.
The final design should communicate an emphasis on recruiting and wellness
The main purpose of the business card is to utilized it for networking events, give to hospitals, executives, VCs surgery centers and clinics. I want it to be sleek, clean, use of our brand colors and professional.

```html
<!DOCTYPE html>
<html lang="en">
<head>
<meta charset="utf-8">
<title>Brivora Collective Business Card</title>
<link rel="stylesheet" href="https://fonts.googleapis.com/css2?family=Open+Sans:wght@400;600;700&display=swap">
<style>
  :root {
    --page: #e9e8e6;
    --card: #1b1c1e;
    --card-deep: #141517;
    --teal: #0f6b5e;
    --ink: #ffffff;
    --muted: #d7d9da;
    --gloss-a: #3a3b3d;
    --gloss-b: #0c0c0d;
  }
  * { box-sizing: border-box; margin: 0; padding: 0; }
  html, body { width: 1200px; height: 786px; overflow: hidden; background: var(--page); }
  body {
    font-family: "Open Sans", Arial, sans-serif;
    display: flex; align-items: center; justify-content: center; gap: 44px;
  }
  .card {
    position: relative; width: 525px; height: 300px;
    background: var(--card); overflow: hidden;
    box-shadow: 0 10px 26px rgba(0,0,0,.25);
  }
  .brand {
    position: absolute; left: 34px; top: 36px;
    display: flex; align-items: center; gap: 10px;
    color: var(--teal); font-weight: 600; font-size: 25px; letter-spacing: .2px;
  }
  .brand-square { width: 22px; height: 22px; background: var(--teal); border-radius: 4px; }
  .accent-bar { position: absolute; left: 0; top: 120px; width: 10px; height: 42px; background: var(--teal); }
  .person { position: absolute; left: 34px; top: 118px; }
  .person-name { color: var(--teal); font-weight: 700; font-size: 20px; text-transform: uppercase; letter-spacing: .4px; line-height: 1.1; }
  .person-title { color: var(--ink); font-size: 15px; margin-top: 3px; }
  .contacts { position: absolute; left: 34px; top: 180px; list-style: none; }
  .contacts li { display: flex; align-items: center; gap: 9px; color: var(--ink); font-size: 14.5px; line-height: 21px; }
  .contacts svg { width: 12px; height: 12px; fill: var(--muted); flex: none; }
  .address { position: absolute; left: 34px; top: 248px; color: var(--ink); font-size: 15px; line-height: 20px; }
  .front-decoration {
    position: absolute; right: 30px; top: 40px; width: 210px; height: 220px;
    border-radius: 14px;
    background: linear-gradient(135deg, var(--gloss-a) 0%, #1e1f21 45%, var(--gloss-b) 100%);
  }
  .back-pattern {
    position: absolute; inset: 0;
    background: linear-gradient(100deg, #4a4b4d 0%, #26272a 30%, var(--card-deep) 60%, #0a0a0b 100%);
  }
  .back-edge { position: absolute; left: 0; right: 0; bottom: 0; height: 8px; background: var(--teal); }
</style>
</head>
<body>
  <section class="card card-front">
    <div class="brand"><span class="brand-square"></span>Brivora Collective</div>
    <div class="accent-bar"></div>
    <div class="person">
      <p class="person-name">Elena Marsh</p>
      <p class="person-title">Managing Director</p>
    </div>
    <ul class="contacts">
      <li><svg viewBox="0 0 24 24"><path d="M6.6 10.8a15 15 0 0 0 6.6 6.6l2.2-2.2a1 1 0 0 1 1-.25 11.4 11.4 0 0 0 3.6.57 1 1 0 0 1 1 1V20a1 1 0 0 1-1 1A17 17 0 0 1 3 4a1 1 0 0 1 1-1h3.5a1 1 0 0 1 1 1c0 1.25.2 2.45.57 3.57a1 1 0 0 1-.25 1z"/></svg>123 456 789</li>
      <li><svg viewBox="0 0 24 24"><path d="M2 5h20v14H2zm2 2v.5l8 5 8-5V7zm0 2.9V17h16V9.9l-8 5z"/></svg>info@yourgmail.com</li>
      <li><svg viewBox="0 0 24 24"><path d="M12 2a10 10 0 1 0 0 20 10 10 0 0 0 0-20zm6.9 9h-3a15 15 0 0 0-1.4-6A8 8 0 0 1 18.9 11zM12 4c.9 1.2 1.7 3.6 1.9 7h-3.8c.2-3.4 1-5.8 1.9-7zM4.1 13h3a15 15 0 0 0 1.4 6A8 8 0 0 1 4.1 13zm3-2h-3a8 8 0 0 1 4.4-6 15 15 0 0 0-1.4 6zM12 20c-.9-1.2-1.7-3.6-1.9-7h3.8c-.2 3.4-1 5.8-1.9 7zm2.5-1a15 15 0 0 0 1.4-6h3a8 8 0 0 1-4.4 6z"/></svg>www.yourwebsite.com</li>
    </ul>
    <p class="address">Your address, City<br>State, Zip 1234</p>
    <div class="front-decoration" role="img" aria-label="Large glossy brand symbol in black spot varnish"></div>
  </section>

  <section class="card card-back">
    <div class="back-pattern" role="img" aria-label="Repeating brand symbol pattern in glossy black varnish"></div>
    <div class="back-edge"></div>
  </section>
</body>
</html>
```